VORTA Diagnostics Pooling One Sheet

The process and concept for pooling is to target large populations of people; i.e. a school, prison, employer (where people are isolated by pods), then to test them all in one controllable group. By breaking down the pool size (ideally is 12 or 16 max) then when a positive pool pops up, the entity has the lab automatically reflex to test the whole pool to determine who is positive. During that exchange, several workflows could take place from the population that was being tested. This type of pooled testing is called Surveillance testing ,when it reflects, then it goes to Screening or Diagnostic testing.

The workflow is:
School/employer collects all patient information captured on a requisition form or electronically (w signature) and DOES NOT send to VORTA
School/employer collects individual specimens and labels them with a unique bar code (non-repeating and can include the DOB)
School/employer is responsible for housing and managing all the unique patient information for each individual specimen
School/employer delivers specimens to VORTA and School/employer directs VORTA what specimens are in what designated pool (one pool size for entire project)
When a pool is positive, VORTA notifies School/employer
When reflex testing in indicated for client, School/employer submits to VORTA on demand all patient information needed to process the reflexed option
VORTA reports back to School/employer in 12 hours the results of the retest
https://www.healthbureau-example.test/medical-devices/coronavirus-covid-19-and-medical-devices/pooled-sample-testing-and-screening-testing-covid-19
https://www.mediquestlabs.test/coronavirus-disease-covid-19/news/mediquest-receives-authorization-covid-19-sample-pooling

Target Market(s)

Schools, Universities, Employers

Font styles to use
Sans Serif

Colors
85acd3
85cae6
34a6d7

Requirements
Must have
• VORTA branded along with an elegant yet clinical feel. have all contact information for VORTA Diagnostics. Go to www.vortadx.test for all info

```html
<!DOCTYPE html>
<html lang="en">
<head>
<meta charset="utf-8">
<title>VORTA Diagnostics – Pooled Sample Testing</title>
<link href="https://fonts.googleapis.com/css2?family=Source+Sans+3:wght@400;600;700&display=swap" rel="stylesheet">
<style>
  :root{
    --teal:#3a9aa9;
    --teal-deep:#2f8796;
    --teal-soft:rgba(58,154,169,.86);
    --ink:#3b3f44;
    --footer-dark:#3a3c40;
    --paper:#ffffff;
    --bg:#e9ecee;
    --rule:#9aa3a8;
  }
  *{box-sizing:border-box;margin:0;padding:0}
  html,body{width:1200px;height:800px;overflow:hidden;background:var(--bg);font-family:"Source Sans 3",Arial,sans-serif}
  .sheet{position:absolute;left:294px;top:3px;width:612px;height:794px;background:var(--paper);overflow:hidden;box-shadow:0 2px 10px rgba(0,0,0,.15)}
  .abs{position:absolute}
  .photo{left:0;top:52px;width:612px;height:306px;background:linear-gradient(100deg,#9fd0e0 0%,#cfe6ee 35%,#eef4f6 60%,#dfe9ed 100%)}
  .header-white{left:0;top:0;width:612px;height:86px}
  .brand{left:22px;top:30px;display:flex;align-items:center;gap:10px}
  .brand-mark{width:26px;height:26px;background:var(--teal)}
  .brand-name{font-size:21px;font-weight:600;color:var(--teal);letter-spacing:.2px}
  .title-tab{left:0;top:0;width:612px;height:52px}
  .title{right:14px;top:11px;color:#fff;font-size:21px;font-weight:700;letter-spacing:.2px}
  .intro{left:20px;top:210px;width:262px;color:#fff;font-size:13.2px;line-height:15.6px;text-align:justify}
  .pool{left:20px;top:315px;width:300px;color:#fff;font-size:11.2px;line-height:14px;letter-spacing:-.2px}
  .band{left:0;top:358px;width:612px;height:61px;background:var(--teal)}
  .band p{position:absolute;left:20px;top:14px;width:585px;color:#fff;font-size:11.2px;line-height:15px;letter-spacing:-.2px}
  .wf-label{left:20px;top:555px;color:var(--teal);font-size:9px;font-weight:700}
  .timeline{left:20px;top:574px;width:580px;height:1px;background:var(--rule)}
  .step{position:absolute;width:110px;font-size:8.2px;line-height:9.2px;color:var(--ink);letter-spacing:-.25px;border-left:1px solid var(--rule);padding-left:4px;text-align:justify}
  .icon{position:absolute;width:54px;height:60px}
  .stem{position:absolute;width:1px;background:var(--teal)}
  .dot{position:absolute;width:5px;height:5px;border-radius:50%;background:var(--teal)}
  .footer{left:0;top:752px;width:612px;height:42px}
  .footer-cta{left:20px;top:764px;color:#fff;font-size:14px;letter-spacing:.2px}
  .footer-url{left:396px;top:761px;color:#fff;font-size:16px;font-weight:700;display:flex;align-items:center;gap:7px}
  .footer-url .accent{color:#6fc6dc}
</style>
</head>
<body>
<svg width="0" height="0" style="position:absolute">
  <defs>
    <symbol id="hex" viewBox="0 0 54 60">
      <polygon points="27,1 52,15 52,45 27,59 2,45 2,15" fill="none" stroke="#3a9aa9" stroke-width="2"/>
      <polygon points="27,7 47,18.5 47,41.5 27,53 7,41.5 7,18.5" fill="#3a9aa9"/>
    </symbol>
  </defs>
</svg>

<main class="sheet">
  <div class="abs photo" role="img" aria-label="Photo of a lab technician in protective suit and goggles handling a sample dish, with a digital cell-analysis overlay"></div>

  <svg class="abs header-white" viewBox="0 0 612 86"><polygon points="0,0 330,0 305,86 0,86" fill="#fff"/></svg>
  <div class="abs brand"><span class="brand-mark"></span><span class="brand-name">VORTA Diagnostics</span></div>

  <svg class="abs title-tab" viewBox="0 0 612 52"><polygon points="336,0 612,0 612,52 320,52" fill="#3a9aa9"/></svg>
  <div class="abs title">POOLED SAMPLE TESTING</div>

  <svg class="abs" style="left:0;top:196px" width="360" height="162" viewBox="0 0 360 162">
    <polygon points="0,0 295,0 325,102 0,102" fill="rgba(58,154,169,.86)"/>
    <polygon points="0,102 325,102 342,162 0,162" fill="#2f8796"/>
  </svg>
  <p class="abs intro">The process and concept for pooling is to target large populations of people; i.e. a school, prison, employer (where people are isolated by pods), then to test them all in one controllable group.</p>
  <p class="abs pool">By breaking down the pool size (ideally is 12 or 16 max) then when a positive pool pops up, the entity has the lab automatically reflex to test the whole pool to determine who is positive.</p>

  <div class="abs band"><p>During that exchange, several workflows could take place from the population that was being tested. This type of pooled testing is called Surveillance testing, when it reflects, then it goes to Screening or Diagnostic testing.</p></div>

  <!-- workflow -->
  <div class="abs wf-label">THE WORKFLOW</div>
  <div class="abs timeline"></div>

  <!-- upper steps -->
  <p class="step" style="left:106px;top:440px">School / employer collects all patient information captured on a requisition form or electronically (w signature) and DOES NOT send to VORTA</p>
  <svg class="icon" style="left:133px;top:497px"><use href="#hex"/><rect x="19" y="20" width="16" height="20" fill="none" stroke="#fff" stroke-width="1.6"/><line x1="22" y1="26" x2="32" y2="26" stroke="#fff" stroke-width="1.4"/><line x1="22" y1="30" x2="32" y2="30" stroke="#fff" stroke-width="1.4"/><line x1="22" y1="34" x2="29" y2="34" stroke="#fff" stroke-width="1.4"/></svg>
  <div class="stem" style="left:160px;top:556px;height:18px"></div><div class="dot" style="left:158px;top:556px"></div>

  <p class="step" style="left:253px;top:440px">School / employer collects individual specimens and labels them with a unique bar code (non-repeating and can include the DOB)</p>
  <svg class="icon" style="left:279px;top:497px"><use href="#hex"/><polygon points="18,27 26,19 36,29 28,37" fill="none" stroke="#fff" stroke-width="1.6"/><circle cx="23" cy="24" r="1.6" fill="#fff"/></svg>
  <div class="stem" style="left:306px;top:556px;height:18px"></div><div class="dot" style="left:304px;top:556px"></div>

  <p class="step" style="left:409px;top:442px">School / employer is responsible for housing and managing all the unique patient information for each individual specimen</p>
  <svg class="icon" style="left:437px;top:497px"><use href="#hex"/><rect x="19" y="20" width="16" height="21" rx="1.5" fill="none" stroke="#fff" stroke-width="1.6"/><rect x="23" y="18" width="8" height="4" fill="#fff"/><line x1="22" y1="28" x2="32" y2="28" stroke="#fff" stroke-width="1.4"/><line x1="22" y1="32" x2="32" y2="32" stroke="#fff" stroke-width="1.4"/><line x1="22" y1="36" x2="32" y2="36" stroke="#fff" stroke-width="1.4"/></svg>
  <div class="stem" style="left:464px;top:556px;height:18px"></div><div class="dot" style="left:462px;top:556px"></div>

  <!-- lower steps -->
  <div class="stem" style="left:88px;top:575px;height:18px"></div><div class="dot" style="left:86px;top:583px"></div>
  <svg class="icon" style="left:61px;top:590px"><use href="#hex"/><path d="M24 18 L30 18 M25 18 L25 30 L19 40 L35 40 L29 30 L29 18" fill="none" stroke="#fff" stroke-width="1.6"/></svg>
  <p class="step" style="left:34px;top:655px">School / employer delivers specimens to VORTA and School / employer directs VORTA what specimens are in what designated pool (one pool size for entire project)</p>

  <div class="stem" style="left:227px;top:575px;height:18px"></div><div class="dot" style="left:225px;top:583px"></div>
  <svg class="icon" style="left:200px;top:590px"><use href="#hex"/><polyline points="19,30 25,36 36,23" fill="none" stroke="#fff" stroke-width="2.2"/></svg>
  <p class="step" style="left:171px;top:657px">When a pool is positive, VORTA notifies School/employer</p>

  <div class="stem" style="left:385px;top:575px;height:18px"></div><div class="dot" style="left:383px;top:583px"></div>
  <svg class="icon" style="left:358px;top:590px"><use href="#hex"/><circle cx="27" cy="26" r="4" fill="#fff"/><circle cx="19" cy="28" r="3" fill="#fff"/><circle cx="35" cy="28" r="3" fill="#fff"/><path d="M20 39 Q27 29 34 39 Z" fill="#fff"/></svg>
  <p class="step" style="left:327px;top:657px">When reflex testing in indicated for client, School / employer submits to VORTA on demand all patient information needed to process the reflexed option</p>

  <div class="stem" style="left:539px;top:575px;height:18px"></div><div class="dot" style="left:537px;top:583px"></div>
  <svg class="icon" style="left:512px;top:590px"><use href="#hex"/><circle cx="29" cy="31" r="8" fill="none" stroke="#fff" stroke-width="1.6"/><line x1="29" y1="31" x2="29" y2="26" stroke="#fff" stroke-width="1.6"/><line x1="27" y1="21" x2="31" y2="21" stroke="#fff" stroke-width="1.6"/><line x1="16" y1="28" x2="20" y2="28" stroke="#fff" stroke-width="1.4"/><line x1="15" y1="32" x2="19" y2="32" stroke="#fff" stroke-width="1.4"/></svg>
  <p class="step" style="left:482px;top:657px">VORTA reports back to School / employer in 12 hours the results of the retest</p>

  <svg class="abs footer" viewBox="0 0 612 42">
    <rect width="612" height="42" fill="#3a3c40"/>
    <polygon points="0,0 355,0 372,42 0,42" fill="#3a9aa9"/>
  </svg>
  <div class="abs footer-cta">VISIT OUR WEBSITE FOR MORE INFORMATION</div>
  <div class="abs footer-url">
    <svg width="16" height="16" viewBox="0 0 16 16"><circle cx="8" cy="8" r="6.5" fill="none" stroke="#fff" stroke-width="1.5"/><line x1="1.5" y1="8" x2="14.5" y2="8" stroke="#fff" stroke-width="1.2"/><ellipse cx="8" cy="8" rx="3" ry="6.5" fill="none" stroke="#fff" stroke-width="1.2"/></svg>
    <span>www.<span class="accent">vortadx</span>.test</span>
  </div>
</main>
</body>
</html>
```